Copper Meadow Creamery Business cards

We need a logo design for our family dairy. Included on the cards should be my name/my husbands name/the dairy name/ all the phone numbers/address and email. The name is Copper Meadow Creamery, LLC. We would like to use our farm mascot pic on the card. We know the pictures I sent you are of a beef cow but she is the mascot of the farm. We were thinking that maybe put a picture of her head in the middle of the card with a "B" on one side and a "D" on the other side with a "C" around the picture of the cow. But we are open to any ideas. We are looking for something kind of professional and a design that that can be used on cards, clothing and a car sign. Black lettering and blue for the other color...or what looks good.

Target Market(s)

All

Industry/Entity Type

Farming

Contact Information for Business Card

Marla Dutton Owner (555)417-2093
Ronald Pfister Owner (555)238-7715
Copper Meadow Creamery, LLC (555)906-4182
Coppermeadowcreamery@mailbarn.test
7126 County Lane 91, Aldenvale, MN 50917

Font styles to use
Sans Serif

Colors
3176b5
3c7bb8
3277b5
0255a3

Requirements
Must have
• Some design that incorporates a drawing/pic of the cow pictures that were sent.
Nice to have
• no suggestions
Should not have
• no suggestions

```html
<!DOCTYPE html>
<html lang="en">
<head>
<meta charset="utf-8">
<title>Copper Meadow Creamery L.L.C. Business Card</title>
<link rel="stylesheet" href="https://fonts.googleapis.com/css2?family=Barlow:wght@400;500;600&display=swap">
<style>
  :root {
    --card-blue: #1372bd;
    --band-blue: #1f88d0;
    --band-edge: #1a7cc4;
    --ring-purple: #2e3196;
    --ink: #0c1930;
    --title-white: #ffffff;
    --strip-light: #8bbbe0;
    --photo-light: #e9e6e4;
    --photo-dark: #3a3634;
  }
  * { margin: 0; padding: 0; box-sizing: border-box; }
  html, body { width: 1200px; height: 667px; overflow: hidden; background: #ffffff; }
  .card {
    position: relative;
    width: 1200px;
    height: 667px;
    background: var(--card-blue);
    overflow: hidden;
    font-family: "Barlow", sans-serif;
    color: var(--ink);
  }
  .title-band {
    position: absolute;
    left: 0; top: 50px;
    width: 1200px; height: 108px;
    background: var(--band-blue);
    border-bottom: 12px solid var(--band-edge);
  }
  .mascot {
    position: absolute;
    left: 0; top: 0;
    width: 420px; height: 460px;
  }
  .company-name {
    position: absolute;
    right: 43px; top: 62px;
    font-size: 50px;
    font-weight: 500;
    color: var(--title-white);
    white-space: nowrap;
    line-height: 1.3;
  }
  .main-phone {
    position: absolute;
    left: 587px; top: 178px;
    font-size: 64px;
    font-weight: 500;
    letter-spacing: 1px;
    line-height: 1.2;
    white-space: nowrap;
  }
  .owner {
    position: absolute;
    top: 340px;
    white-space: nowrap;
  }
  .owner--first { left: 437px; }
  .owner--second { left: 776px; }
  .owner-name { font-size: 48px; font-weight: 500; line-height: 1.1; }
  .owner-role { font-size: 26px; font-weight: 400; line-height: 1.1; margin-top: 2px; }
  .owner-phone { font-size: 38px; font-weight: 400; line-height: 1.2; margin-top: 4px; letter-spacing: 0.5px; }
  .divider {
    position: absolute;
    left: 721px; top: 335px;
    width: 3px; height: 148px;
    background: var(--ink);
  }
  .contact-strip {
    position: absolute;
    left: 0; top: 577px;
    width: 1200px; height: 57px;
    background: var(--strip-light);
    display: flex;
    align-items: center;
    justify-content: space-between;
    padding: 0 68px 0 72px;
    white-space: nowrap;
  }
  .address { font-size: 29px; font-weight: 600; }
  .email { font-size: 25px; font-weight: 500; }
</style>
</head>
<body>
  <div class="card">
    <div class="title-band"></div>

    <svg class="mascot" viewBox="0 0 420 460">
      <defs>
        <radialGradient id="mascotTone" cx="45%" cy="40%" r="65%">
          <stop offset="0%" stop-color="var(--photo-light)"/>
          <stop offset="60%" stop-color="#cfc9c6"/>
          <stop offset="100%" stop-color="var(--photo-dark)"/>
        </radialGradient>
      </defs>
      <circle cx="204" cy="222" r="195" fill="var(--ring-purple)" opacity="0.35"/>
      <circle cx="198" cy="216" r="195" fill="var(--ring-purple)"/>
      <circle cx="165" cy="185" r="170" fill="url(#mascotTone)" role="img" aria-label="Photo of the farm mascot cow's head"/>
    </svg>

    <div class="company-name">Copper Meadow Creamery L.L.C.</div>

    <div class="main-phone">(555)906-4182</div>

    <div class="owner owner--first">
      <div class="owner-name">Marla Dutton</div>
      <div class="owner-role">Owner</div>
      <div class="owner-phone">(555)417-2093</div>
    </div>

    <div class="divider"></div>

    <div class="owner owner--second">
      <div class="owner-name">Ronald Pfister</div>
      <div class="owner-role">Owner</div>
      <div class="owner-phone">(555)238-7715</div>
    </div>

    <div class="contact-strip">
      <span class="address">7126 County Lane 91, Aldenvale, MN 50917</span>
      <span class="email">coppermeadowcreamery@mailbarn.test</span>
    </div>
  </div>
</body>
</html>
```